Flyer-Design für Tauchsafaris, Vollcharter und Mini Safaris am roten Meer
Zielgruppe
Korvo Diving Safari
Wir sind ein Unternehmen, welches im Roten Meer Tauchsafaris, Vollcharter und Mini Safaris durchführt. Unsere Zielgruppe sind Taucher. Wir benötigen einen ansprechenden Flyer, welchen wir an Messen und auf den Booten an pozenziellen Kunden weitergeben können.
Aufgabenstellung
Der Flyer wird in Englisch sein. Anbei ist eine Worddatei angehängt mit den Textvorschlägen, die wir mal so besprochen haben. Das Layout muss nicht beachtet werden, es hat uns nur zur Übersich gedient. Unser jetztiger Flyer ist ein Falzflyer über 6 Seiten. Aber vielleicht macht auch ein anderers Mass sinn.
Wir haben sehr viele Bilder zur Verfügung, wenn etwas spezielles gebraucht wird.

```html
<!DOCTYPE html>
<html lang="en">
<head>
<meta charset="utf-8">
<title>Korvo Diving Safari – Tri-fold Flyer</title>
<link rel="stylesheet" href="https://fonts.googleapis.com/css2?family=Lexend:wght@400;500;600&display=swap">
<style>
  :root {
    --backdrop: #3b3d40;
    --navy: #1d4f8c;
    --ocean: #1762a8;
    --ocean-deep: #0f3f78;
    --teal: #2a8fbb;
    --teal-light: #3aa3c9;
    --paper: #ffffff;
    --paper-grey: #e6e9ee;
    --text-blue: #22508a;
    --ink: #2b4670;
  }
  * { box-sizing: border-box; margin: 0; padding: 0; }
  html, body { width: 1200px; height: 818px; overflow: hidden; }
  body {
    background: var(--backdrop);
    font-family: "Lexend", "Helvetica Neue", Arial, sans-serif;
    color: var(--text-blue);
  }
  .flyer {
    position: absolute;
    left: 60px; top: 29px;
    width: 1080px; height: 760px;
    display: flex;
    box-shadow: 0 10px 30px rgba(0,0,0,.45);
  }
  .panel {
    position: relative;
    width: 360px; height: 760px;
    overflow: hidden;
    background: var(--paper);
  }
  .photo { position: absolute; left: 0; top: 0; width: 100%; }
  .brand-tag {
    position: absolute; left: 12px; top: 12px;
    background: var(--paper);
    padding: 5px 8px;
    display: flex; align-items: center; gap: 5px;
    font-size: 8px; font-weight: 500; color: var(--navy);
    text-transform: uppercase; letter-spacing: .3px;
  }
  .brand-tag .dot { width: 12px; height: 12px; border-radius: 50%; background: var(--navy); }

  /* contact panel */
  .contact .photo { height: 275px; background: linear-gradient(170deg, #5d9fd6 0%, #2e78bf 45%, #1a5ea6 100%); }
  .contact h2 {
    position: absolute; top: 305px; width: 100%;
    text-align: center; font-size: 25px; font-weight: 600; color: var(--navy);
  }
  .contact-list { position: absolute; top: 365px; left: 40px; list-style: none; }
  .contact-list li {
    display: flex; align-items: center; gap: 14px;
    font-size: 15px; color: var(--text-blue); height: 36px;
  }
  .contact-list li.indent { padding-left: 52px; margin-top: -4px; }
  .contact-list li.gap { margin-top: 22px; }
  .icon { width: 30px; height: 30px; flex: none; }
  .social-dot { width: 26px; height: 26px; border-radius: 50%; background: var(--navy); flex: none; margin: 0 2px; }

  /* about panel */
  .about { background: linear-gradient(180deg, var(--paper-grey), #d9dde3); }
  .about .photo { height: 275px; background: linear-gradient(180deg, #a7c3de 0%, #d7dfe6 40%, #7fa6cf 75%, #e5e8ec 100%); }
  .about-text { position: absolute; top: 300px; left: 30px; right: 28px; font-size: 12.5px; line-height: 1.45; color: var(--text-blue); }
  .about-text h3 { font-size: 14px; font-weight: 600; }
  .about-text p { margin-bottom: 16px; }

  /* cover panel */
  .cover .photo { height: 210px; background: radial-gradient(ellipse at 50% 40%, #2d8fd0 0%, #1565ad 55%, #0b3f7c 100%); }
  .welcome { position: absolute; top: 210px; width: 100%; height: 95px; text-align: center; padding-top: 14px; }
  .welcome small { display: block; font-size: 13px; font-weight: 500; color: var(--ocean); }
  .welcome h1 { font-size: 23px; font-weight: 600; color: var(--ocean); line-height: 1.2; }
  .welcome .label { display: block; font-size: 11px; color: var(--ocean); margin-top: 8px; }
  .services {
    position: absolute; top: 305px; width: 100%; height: 280px;
    display: grid; grid-template-columns: repeat(3, 1fr); grid-template-rows: 1fr 1fr;
  }
  .service {
    display: flex; align-items: center; justify-content: center; text-align: center;
    color: #fff; font-size: 12.5px; line-height: 1.3; padding: 8px;
  }
  .s1 { background: var(--ocean); } .s2 { background: var(--teal); } .s3 { background: var(--ocean-deep); }
  .s4 { background: var(--teal-light); } .s5 { background: var(--ocean); } .s6 { background: var(--teal); }
  .cover-foot {
    position: absolute; top: 585px; width: 100%; height: 175px;
    background: linear-gradient(180deg, var(--paper) 0 12px, #1a5fa6 12px, #0e4281 100%);
    display: flex; align-items: center; justify-content: center; text-align: center;
    color: #fff; font-size: 19px; font-weight: 500; line-height: 1.3; padding-top: 10px;
  }
</style>
</head>
<body>
<main class="flyer">
  <section class="panel contact">
    <div class="photo" role="img" aria-label="Photo of a shark swimming in blue water"></div>
    <div class="brand-tag"><span class="dot"></span>Korvo Diving Safari</div>
    <h2>Let's get in touch!</h2>
    <ul class="contact-list">
      <li>
        <svg class="icon" viewBox="0 0 30 30"><circle cx="15" cy="15" r="14" fill="var(--navy)"/><g fill="none" stroke="#fff" stroke-width="1.4"><circle cx="15" cy="15" r="8"/><ellipse cx="15" cy="15" rx="3.5" ry="8"/><line x1="7" y1="15" x2="23" y2="15"/></g></svg>
        korvodivingsafari.com
      </li>
      <li class="gap">
        <svg class="icon" viewBox="0 0 30 30"><circle cx="15" cy="15" r="14" fill="var(--navy)"/><g fill="none" stroke="#fff" stroke-width="1.4"><rect x="8" y="10" width="14" height="10"/><polyline points="8,10 15,16 22,10"/></g></svg>
        info@korvodiving
      </li>
      <li class="gap">
        <svg class="icon" viewBox="0 0 30 30"><circle cx="15" cy="15" r="14" fill="var(--navy)"/><g fill="none" stroke="#fff" stroke-width="1.4"><rect x="11" y="7" width="8" height="16" rx="1.5"/><line x1="14" y1="20.5" x2="16" y2="20.5"/></g></svg>
        Amir: +20 xyzxyzxyz
      </li>
      <li class="indent">Karim: +20 xyxyxyx</li>
      <li class="indent">Leila: +20 xyxyxyx</li>
      <li class="gap"><span class="social-dot"></span>Korvo Diving Safari</li>
      <li class="gap"><span class="social-dot"></span>Korvo Diving</li>
      <li class="gap"><span class="social-dot"></span>@korvo_diving_safari</li>
    </ul>
  </section>

  <section class="panel about">
    <div class="photo" role="img" aria-label="Photo of the dive team waving a banner on the deck of a boat at sea"></div>
    <div class="brand-tag"><span class="dot"></span>Korvo Diving Safari</div>
    <div class="about-text">
      <h3>About us</h3>
      <p>For more than 7 years we have been proud to arrange your diving adventure in the Red Sea of Egypt. Made by divers, for divers with more than 10 years of experience.</p>
      <p>We are specialized in diving safaris, full charter and mini safaris. Our ultimate ambition is to make your wishes come true.</p>
      <p>Whether you are an experienced diver or have just started your diving adventure. We want to take you away from everyday life and immerse you in the colourful world of corals and fish.</p>
      <p>Our team is at home in the Red Sea and knows the finest places and shows you with passion the variety of countless dive sites coasts nearby and far.</p>
    </div>
  </section>

  <section class="panel cover">
    <div class="photo" role="img" aria-label="Underwater photo of a group of divers holding a banner"></div>
    <div class="brand-tag"><span class="dot"></span>Korvo Diving Safari</div>
    <div class="welcome">
      <small>Welcome to</small>
      <h1>Korvo Diving Safari</h1>
      <span class="label">our services:</span>
    </div>
    <div class="services">
      <div class="service s1">Individual<br>Liveaboards</div>
      <div class="service s2">Fullcharter</div>
      <div class="service s3">Mini<br>Safari</div>
      <div class="service s4">Beach<br>Dives</div>
      <div class="service s5">Daily<br>Boat</div>
      <div class="service s6">Full range of<br>OCEANCERT<br>courses</div>
    </div>
    <div class="cover-foot">Discover the beauty of<br>the Red Sea with us!</div>
  </section>
</main>
</body>
</html>
```